Ethiopian Restaurant Web Design

San Diego, CA's oldest Ethiopian Restaurant, is redesigning its website. We need to get some designs that embrace the culture and flavors of Ethiopia. They are often featured in local magazines and news stories and we need their site to shine.

Number of Pages Required

3 page

Other font styles liked:
• http://www.goldfernkitchensd.com

```html
<!DOCTYPE html>
<html lang="en">
<head>
<meta charset="utf-8">
<title>Gold Fern Ethiopian Kitchen</title>
<link rel="stylesheet" href="https://fonts.googleapis.com/css2?family=Kaushan+Script&family=Lato:wght@400;700;900&display=swap">
<style>
:root{
  --red:#b40c0c;
  --red-deep:#8e0707;
  --maroon:#3b0b08;
  --maroon-card:#4a1410;
  --gold:#f7cf7f;
  --gold-dark:#e9b85d;
  --ink:#222;
  --muted:#555;
  --paper:#fff;
  --fog:#f1f0ef;
  --charcoal:#3a3a3a;
  --field:#8c8c8c;
  --forest:#0f2a1f;
  --pink:#e9a3a3;
}
*{box-sizing:border-box;margin:0;padding:0}
html,body{width:1200px;height:4914px;overflow:hidden}
body{font-family:"Lato",sans-serif;color:var(--ink);background:var(--paper);position:relative}
.abs{position:absolute}
.script{font-family:"Kaushan Script",cursive;font-weight:400}
.photo{position:absolute}
.btn{position:absolute;display:flex;align-items:center;justify-content:center;font-weight:700;font-size:15px;border-radius:3px}
.btn-gold{background:var(--gold);color:var(--red)}
.btn-red{background:var(--red);color:#fff}

/* nav */
.nav-bar{top:0;left:0;width:1200px;height:57px;background:var(--red);z-index:5}
.brand{top:0;left:153px;width:144px;height:76px;background:#fff;z-index:6;display:flex;align-items:center;justify-content:center;font-weight:900;font-size:20px;color:var(--red)}
.menu{top:0;left:458px;height:57px;display:flex;align-items:center;gap:22px;z-index:6;color:#fff;font-size:12px}
.menu .current{color:var(--gold);font-weight:700}
.book{top:12px;left:966px;width:83px;height:30px;z-index:6;font-size:12px}

/* hero */
.hero-photo{top:0;left:0;width:1200px;height:650px;background:linear-gradient(110deg,#3b2417 0%,#5a3624 40%,#4a2c1e 70%,#2e1b12 100%)}
.dish{top:30px;left:690px;width:450px;height:520px;border-radius:50%;background:radial-gradient(circle,#7a5a2a 0%,#4d3a1f 45%,#2a1a12 72%,transparent 73%)}
.hero-title{top:170px;left:162px;color:#fff;z-index:2}
.hero-title .best{font-weight:900;font-size:62px;line-height:1}
.hero-title .gold{color:var(--gold);font-size:70px;line-height:1.05}
.hero-title .white{color:#fff;font-size:70px;line-height:1}
.hero-btn{top:410px;left:168px;width:175px;height:68px;font-size:16px}

/* about */
.chef{top:553px;left:150px;width:290px;height:440px;background:linear-gradient(180deg,#f3f3f3,#e2ddd8);border-radius:140px 140px 10px 10px}
.eyebrow{top:710px;left:534px;font-size:12px;color:var(--ink)}
.about-title{top:728px;left:532px;font-size:46px;color:var(--red)}
.about-text{top:798px;left:534px;width:500px;font-size:12.5px;line-height:19px;color:var(--ink)}
.plate-side{top:935px;left:1072px;width:150px;height:150px;border-radius:50%;background:radial-gradient(circle,#c9a46a,#8a6b43 70%,#ddd 71%)}

/* services */
.services{top:1000px;left:0;width:1200px;height:660px;background:var(--red)}
.services-title{top:1095px;left:0;width:1200px;text-align:center;font-size:46px;color:#fff}
.services-text{top:1168px;left:235px;width:730px;text-align:center;color:#fff;font-size:12.5px;line-height:19px}
.svc{position:absolute;top:1290px;width:230px;text-align:center;color:#fff}
.svc svg{display:block;margin:0 auto}
.svc h3{font-family:"Kaushan Script",cursive;font-weight:400;font-size:25px;color:var(--gold);margin-top:22px}
.svc p{font-size:12.5px;line-height:19px;margin-top:14px}
.mint{top:1540px;left:0;width:105px;height:180px;background:radial-gradient(ellipse at 40% 50%,#3c8a2e,#1f5a18 70%,transparent 71%)}

/* coffee */
.coffee-title{top:1765px;left:162px;font-size:46px;color:var(--red)}
.coffee-text{top:1838px;left:165px;width:360px;font-size:12.5px;line-height:19px}
.coffee-btn{top:1965px;left:160px;width:150px;height:48px}
.coffee-photo{top:1752px;left:607px;width:496px;height:308px;background:radial-gradient(ellipse at 55% 45%,#e9e6e2 0%,#9c8670 35%,#3a2518 75%)}
.beans{top:2015px;left:0;width:210px;height:105px;background:radial-gradient(ellipse at 40% 60%,#7a4a28,#4a2a14 70%,transparent 71%)}

/* gursha */
.gursha{top:2118px;left:0;width:1200px;height:534px;background:linear-gradient(90deg,#2e0906,var(--maroon) 50%,#2c0806)}
.gursha-card{top:2185px;left:72px;width:1092px;height:400px;background:var(--maroon-card);border-radius:6px}
.gursha-photo{top:2232px;left:168px;width:267px;height:315px;background:linear-gradient(160deg,#d8cfc3,#b68b52 55%,#6c4a2c);border-radius:12px 110px 110px 12px}
.gursha-title{top:2226px;left:536px;font-size:46px;color:#fff}
.gursha-text{top:2310px;left:535px;width:460px;font-size:12.5px;line-height:19px;color:#fff}
.gursha-btn{top:2480px;left:536px;width:147px;height:54px}

/* menu */
.menu-sec{top:2652px;left:0;width:1200px;height:650px;background:var(--fog)}
.menu-title{top:2700px;left:0;width:1200px;text-align:center;font-size:46px;color:var(--red)}
.menu-intro{top:2776px;left:310px;width:580px;text-align:center;font-size:12.5px;line-height:19px}
.cats{top:2830px;left:160px;font-size:12px;line-height:61px}
.cats .on{color:var(--red)}
.divider{top:2824px;left:311px;width:2px;height:305px;background:#bbb}
.dish-row{position:absolute;left:391px;width:644px}
.dish-row .head{display:flex;align-items:center;color:var(--red);font-weight:700;font-size:15px}
.dish-row .head .dots{flex:1;border-top:1px solid #d88;margin:0 22px}
.dish-row p{font-size:12.5px;line-height:17px;margin:7px 0 0 30px;width:400px}
.menu-btn{top:3135px;height:48px;width:150px;font-size:12px;font-weight:400}

/* gallery */
.gallery-title{top:3380px;left:0;width:1200px;text-align:center;font-size:46px;color:var(--red)}
.gallery-text{top:3458px;left:235px;width:730px;text-align:center;font-size:12.5px;line-height:17px}
.tile{position:absolute;border-radius:2px}
.view-more{top:3796px;left:818px;width:163px;height:50px;font-size:16px;font-weight:400}

/* hours & contact */
.hours-band{top:4010px;left:0;width:460px;height:470px;background:var(--red-deep)}
.hours-title{top:4140px;left:160px;font-size:34px;color:var(--gold)}
.hours-table{top:4200px;left:160px;color:#fff;font-size:12.5px;border-collapse:collapse}
.hours-table th{text-align:left;font-size:15px;padding-bottom:6px}
.hours-table td{padding:2px 0;line-height:18px}
.hours-table td:first-child,.hours-table th:first-child{width:115px}
.contact{top:3969px;left:460px;width:740px;height:524px;background:linear-gradient(180deg,#3c3c3c,#2b2b2b)}
.contact-title{top:4006px;left:460px;width:580px;text-align:center;font-size:34px;color:#fff}
.field{position:absolute;left:534px;width:430px;height:42px;background:var(--field);border-radius:21px;color:#fff;font-size:12px;padding:0 36px;display:flex;align-items:center}
.send{top:4392px;left:677px;width:147px;height:50px;font-size:16px}

/* footer */
.footer{top:4551px;left:0;width:1200px;height:363px;background:var(--forest);color:#fff}
.foot-brand{top:4642px;left:160px;width:130px;height:67px;background:#fff;display:flex;align-items:center;justify-content:center;font-weight:900;font-size:18px;color:var(--red)}
.foot-about{top:4730px;left:160px;width:210px;font-size:11px;line-height:17px;color:#fff}
.social{position:absolute;top:4813px;width:28px;height:28px;border:1.5px solid #fff;border-radius:50%}
.fcol{position:absolute;top:4660px;font-size:11px;line-height:19px;color:#fff}
.fcol h4{color:var(--gold);font-weight:400;font-size:15px;margin-bottom:12px}
.fcol .on{color:var(--gold);font-weight:700}
.copyright{top:4876px;left:0;width:1200px;text-align:center;font-size:10px;color:#fff}
</style>
</head>
<body>

<!-- hero -->
<div class="photo hero-photo abs" role="img" aria-label="Dark rustic wooden table with burlap, basil leaves and spices"></div>
<div class="photo dish abs" role="img" aria-label="Bowl of roasted vegetables with olives, peppers and basil"></div>
<svg class="abs" style="top:560px;left:0" width="1200" height="110" viewBox="0 0 1200 110" aria-hidden="true">
  <path d="M0 70 L60 50 L120 72 L190 55 L260 80 L330 60 L400 78 L470 58 L540 76 L610 52 L680 74 L750 56 L820 80 L890 60 L960 75 L1030 55 L1100 72 L1200 58 L1200 110 L0 110 Z" fill="#fff"/>
</svg>

<div class="abs nav-bar"></div>
<div class="abs brand">Gold Fern</div>
<nav class="abs menu">
  <span class="current">About Us</span><span>Ethiopian Coffee Services</span><span>What is Gursha?</span><span>Menu</span><span>Gallery</span><span>Hours</span>
</nav>
<div class="btn btn-gold book">Book Now</div>

<div class="abs hero-title">
  <div class="best">Best</div>
  <div class="script gold">Ethiopian</div>
  <div class="script white">Food</div>
</div>
<div class="btn btn-gold hero-btn">Book Your Table</div>

<!-- about -->
<div class="photo chef abs" role="img" aria-label="Smiling chef in white hat holding a plate of salad"></div>
<div class="abs eyebrow">About Us</div>
<h1 class="abs script about-title">Welcome! Selam</h1>
<p class="abs about-text">Welcome to Gold Fern Ethiopian Kitchen in San Diego, one of the oldest authentic Ethiopian restaurant in San Diego serving you with pride and joy for several years. We are back with new look to serve you the traditional Ethiopia food and make you to discover Ethiopian culinary art with out traveling several thousands to Ethiopia. We are located in the heart of historic San Diego City Height neighborhoods easy by access by car, bus, walking even biking. Come and visit us, enjoy Ethiopian food.</p>

<!-- services -->
<div class="abs services"></div>
<svg class="abs" style="top:960px;left:0" width="1200" height="60" viewBox="0 0 1200 60" aria-hidden="true">
  <path d="M0 60 L0 45 L70 25 L140 40 L210 18 L290 35 L360 20 L440 38 L520 15 L600 30 L680 12 L760 32 L840 18 L920 36 L1000 20 L1080 34 L1200 22 L1200 60 Z" fill="var(--red)"/>
</svg>
<svg class="abs" style="top:1640px;left:0" width="1200" height="60" viewBox="0 0 1200 60" aria-hidden="true">
  <path d="M0 0 L1200 0 L1200 30 L1120 45 L1040 28 L960 48 L880 30 L800 50 L720 32 L640 46 L560 26 L480 44 L400 28 L320 48 L240 30 L160 46 L80 30 L0 42 Z" fill="var(--red)"/>
</svg>
<div class="photo plate-side abs" role="img" aria-label="Platter of injera with stews"></div>
<h2 class="abs script services-title">Our Services</h2>
<p class="abs services-text">We have variety of services that will cater small or large groups. Our restaurant can hold up to seventy people and soon we are planning to expand our hall and remodel the entire dining area. When the construction completes we can cater more customers. We are able to cater corporate meetings , small weddings, engagement parties, baby and wedding showers, receptions, organization and community sponsored parties, anniversaries and other special occasions, please give us a call ahead of time to reserve our hall for your event and to give the best price in town.</p>

<div class="svc" style="left:181px">
  <svg width="140" height="84" viewBox="0 0 140 84" aria-hidden="true"><path d="M8 40 L130 30 L126 70 L12 78 Z" fill="var(--pink)" opacity=".8"/><circle cx="68" cy="40" r="26" fill="none" stroke="#fff" stroke-width="3"/><circle cx="68" cy="40" r="17" fill="none" stroke="#fff" stroke-width="2"/><path d="M34 14 V66 M28 14 V30 Q34 36 40 30 V14 M102 14 Q96 30 102 42 V66" stroke="#fff" stroke-width="3" fill="none"/></svg>
  <h3>Lorem Ipsum</h3>
  <p>Lorem ipsum dolor sit amet, consectetur adipiscing elit, sed do eiusmod tempor incididunt ut labore et dolore magna aliqua. Ut enim ad minim veniam, quis nostrud exercitation</p>
</div>
<div class="svc" style="left:479px">
  <svg width="140" height="84" viewBox="0 0 140 84" aria-hidden="true"><path d="M8 40 L130 30 L126 70 L12 78 Z" fill="var(--pink)" opacity=".8"/><path d="M36 54 Q36 22 68 22 Q100 22 100 54 Z" fill="none" stroke="#fff" stroke-width="3"/><path d="M28 58 H108" stroke="#fff" stroke-width="3"/><circle cx="68" cy="17" r="4" fill="none" stroke="#fff" stroke-width="3"/></svg>
  <h3>Lorem Ipsum</h3>
  <p>Lorem ipsum dolor sit amet, consectetur adipiscing elit, sed do eiusmod tempor incididunt ut labore et dolore magna aliqua. Ut enim ad minim veniam, quis nostrud exercitation</p>
</div>
<div class="svc" style="left:791px">
  <svg width="140" height="84" viewBox="0 0 140 84" aria-hidden="true"><path d="M8 40 L130 30 L126 70 L12 78 Z" fill="var(--pink)" opacity=".8"/><circle cx="68" cy="40" r="26" fill="none" stroke="#fff" stroke-width="3"/><circle cx="68" cy="40" r="17" fill="none" stroke="#fff" stroke-width="2"/><path d="M34 14 V66 M28 14 V30 Q34 36 40 30 V14 M102 14 Q96 30 102 42 V66" stroke="#fff" stroke-width="3" fill="none"/></svg>
  <h3>Lorem Ipsum</h3>
  <p>Lorem ipsum dolor sit amet, consectetur adipiscing elit, sed do eiusmod tempor incididunt ut labore et dolore magna aliqua. Ut enim ad minim veniam, quis nostrud exercitation</p>
</div>
<div class="photo mint abs" role="img" aria-label="Fresh mint leaves"></div>

<!-- coffee -->
<h2 class="abs script coffee-title">Ethiopian Coffee</h2>
<p class="abs coffee-text">Ethiopia is the birth place of Coffee. At Gold Fern Ethiopian Kitchen we have an authentic way of &nbsp;drinking coffee. It is a unique experience watching your coffee from roasting &nbsp;a green Ethiopian coffee up to serving it. Perhaps it will</p>
<div class="btn btn-red coffee-btn">Read More</div>
<div class="photo coffee-photo abs" role="img" aria-label="White cup of black coffee on a saucer surrounded by coffee beans and cinnamon"></div>
<div class="photo beans abs" role="img" aria-label="Wooden bowl and scoop of roasted coffee beans"></div>

<!-- gursha -->
<div class="abs gursha" role="img" aria-label="Dimmed background of a shared Ethiopian meal"></div>
<div class="abs gursha-card"></div>
<div class="photo gursha-photo abs" role="img" aria-label="Two people feeding each other a bite of food across a table"></div>
<h2 class="abs script gursha-title">What is Gursha?</h2>
<p class="abs gursha-text">The Ethiopia custom of giving gursha plays up the erotic component of eating. Gursha means mouthful and refers to a morsel of food, which one places carefully in anther's mouth, usually as a gesture of affection. Gursha is exchanged between husband and wife, as well as among relatives and friends. We would like to you to experience the art of Gursha - the enjoyment of this custom to its fullest. Simply use your injera to scoop up some food and place it gently in the other person's mouth...with a smile on your lips and twinkle in your</p>
<div class="btn btn-gold gursha-btn">Read More</div>

<!-- menu -->
<div class="abs menu-sec" role="img" aria-label="Faint light background of sketched food and spices"></div>
<h2 class="abs script menu-title">Our Menu</h2>
<p class="abs menu-intro">Hello! Welcome to Ethiopia! Gold Fern Ethiopian Kitchen is one of the oldest Ethiopian Restaurants in San Diego. For more...</p>
<div class="abs cats">
  <div class="on">01.Appetizers</div><div>02.Entrees</div><div>03.Vegetarian Entrees</div><div>04.Vegetarian Entrees</div><div>05.Beverages</div>
</div>
<div class="abs divider"></div>
<div class="dish-row" style="top:2852px"><div class="head"><span>01. &nbsp;Green Salad (Ethiopian Style)</span><span class="dots"></span><span>$7.99</span></div><p>Green salad, tomatoes and onions with home dressing.</p></div>
<div class="dish-row" style="top:2950px"><div class="head"><span>02. &nbsp;Timatim Selata</span><span class="dots"></span><span>$7.99</span></div><p>Fresh tomatoes sliced in our style with green pepper, onion slices and home dressing.</p></div>
<div class="dish-row" style="top:3048px"><div class="head"><span>03. &nbsp;Sambussa</span><span class="dots"></span><span>$2.50</span></div><p>Pastry shell filled with our choice of either: Lentils and green peppers spiced with cumin, green onion with a touch of nutmeg.</p></div>
<div class="btn btn-red menu-btn" style="left:160px">View Full Menu</div>
<div class="btn btn-red menu-btn" style="left:891px">Download PDF &#8595;</div>

<!-- gallery -->
<h2 class="abs script gallery-title">Our Gallery</h2>
<p class="abs gallery-text">Lorem ipsum dolor sit amet, consectetur adipiscing elit, sed do eiusmod tempor incididunt ut labore et dolore magna aliqua. Ut enim ad minim veniam, quis nostrud exercitation ullamco laboris nisi ut aliquip ex ea commodo consequat. Duis aute irure dolor in reprehenderit</p>
<div class="tile" style="top:3535px;left:160px;width:281px;height:373px;background:linear-gradient(160deg,#c9cfb0,#a0521f 45%,#5a2a12)" role="img" aria-label="Glazed grilled chicken wings with sesame on a board"></div>
<div class="tile" style="top:3535px;left:458px;width:280px;height:176px;background:radial-gradient(circle,#8a4a2a,#2a2a2a 70%)" role="img" aria-label="Stir-fried beef with peppers on a dark plate"></div>
<div class="tile" style="top:3732px;left:458px;width:280px;height:176px;background:radial-gradient(circle,#f2f2f2 20%,#5a3a25 45%,#2a2a2a 75%)" role="img" aria-label="Plated sliced meat with greens"></div>
<div class="tile" style="top:3535px;left:759px;width:279px;height:176px;background:linear-gradient(140deg,#6a6a6a,#7a3a24 50%,#3a3a3a)" role="img" aria-label="Grilled steak with fresh vegetables"></div>
<div class="tile" style="top:3732px;left:759px;width:279px;height:176px;background:linear-gradient(140deg,#b43a2a,#8e2418)" role="img" aria-label="Red spices and chili dishes"></div>
<div class="btn btn-gold view-more">View More</div>

<!-- hours & contact -->
<div class="abs hours-band"></div>
<svg class="abs" style="top:3990px;left:0" width="460" height="40" viewBox="0 0 460 40" aria-hidden="true"><path d="M0 40 L0 22 L60 8 L130 24 L200 6 L270 22 L340 10 L400 24 L460 14 L460 40 Z" fill="var(--red-deep)"/></svg>
<svg class="abs" style="top:4470px;left:0" width="460" height="40" viewBox="0 0 460 40" aria-hidden="true"><path d="M0 0 L460 0 L460 20 L390 34 L320 16 L250 32 L180 14 L110 30 L40 18 L0 28 Z" fill="var(--red-deep)"/></svg>
<h2 class="abs script hours-title">Hours</h2>
<table class="abs hours-table">
  <tr><th>Day</th><th>Hours</th></tr>
  <tr><td>Sunday</td><td>12–10PM</td></tr>
  <tr><td>Monday</td><td>CLOSED</td></tr>
  <tr><td>Tuesday</td><td>12–10PM</td></tr>
  <tr><td>Wednesday</td><td>12–10PM</td></tr>
  <tr><td>Thursday</td><td>12–10PM</td></tr>
  <tr><td>Friday</td><td>12–10PM</td></tr>
  <tr><td>Saturday</td><td>12–10PM</td></tr>
</table>
<div class="abs contact" role="img" aria-label="Dark background of a cooking pan"></div>
<h2 class="abs script contact-title">Get In Touch</h2>
<div class="field" style="top:4087px">Name</div>
<div class="field" style="top:4153px">Email I.D</div>
<div class="field" style="top:4222px">Phone No</div>
<div class="field" style="top:4290px;height:70px;border-radius:30px">Subject</div>
<div class="btn btn-gold send">Send</div>

<!-- footer -->
<div class="abs footer"></div>
<svg class="abs" style="top:4530px;left:0" width="1200" height="40" viewBox="0 0 1200 40" aria-hidden="true"><path d="M0 40 L0 22 L80 10 L160 24 L240 8 L320 22 L400 12 L480 26 L560 10 L640 24 L720 8 L800 22 L880 12 L960 26 L1040 10 L1120 22 L1200 12 L1200 40 Z" fill="var(--forest)"/></svg>
<div class="abs foot-brand">Gold Fern</div>
<p class="abs foot-about">Lorem ipsum dolor sit amet, consectetur adipiscing elit, sed do eiusmod tempor incididunt ut labore et dolore magna aliqua.</p>
<span class="social" style="left:158px" aria-label="Social link"></span>
<span class="social" style="left:197px" aria-label="Social link"></span>
<span class="social" style="left:237px" aria-label="Social link"></span>
<span class="social" style="left:277px" aria-label="Social link"></span>
<div class="fcol" style="left:462px"><h4>Quick Links</h4><div class="on">About Us</div><div>Ethiopian Coffee Services</div><div>What is Gursha?</div><div>Menu</div><div>Gallery</div><div>Hours</div></div>
<div class="fcol" style="left:687px"><h4>Services</h4><div>Lorem Ipsum</div><div>Lorem Ipsum</div><div>Lorem Ipsum</div><div>Lorem Ipsum</div><div>Lorem Ipsum</div><div>Lorem Ipsum</div></div>
<div class="fcol" style="left:836px;width:200px"><h4>Contact Us</h4><div>Address: 2280 Juniper Ave, San Diego, CA 92104</div><div style="margin-top:18px">Phone: (619) 555-0148</div><div style="margin-top:18px">Email: hello@goldfernkitchen.com</div></div>
<div class="abs copyright">Copyright © 2022 Gold Fern Ethiopian Kitchen in San Diego</div>

</body>
</html>
```